Improve My Resume Design to be easier for the reader and the recruiter

I need to improve my resume design to make it easier to read and attract employer eyes in a very professional way. And the graphs should be neat, nice and professional. - You can use the below logos as the companies that I worked with are so famous.

Detailed information about me is inside the CV.

Target Market(s)

Big Companies and Famous recruiters

Industry/Entity Type

Government

Colors

Designer to choose colors to be used in the design.

Requirements
Must have
• Infographics .. Easy to Read.
Nice to have
• Charts, infographics.
Should not have
• not professional colours.

```html
<!DOCTYPE html>
<html lang="en">
<head>
<meta charset="utf-8">
<title>Khalid Nasser Omar Haddad – Senior Project Manager</title>
<link href="https://fonts.googleapis.com/css2?family=Ubuntu:wght@400;500;700&family=Open+Sans:wght@400;600;700&display=swap" rel="stylesheet">
<style>
  :root{
    --blue:#1372bb;
    --blue-dark:#0f4f8f;
    --ink:#2b2b2b;
    --text:#222;
    --grey-frame:#58585a;
    --track:#e6e6e6;
    --rule:#6d6d6d;
  }
  *{margin:0;padding:0;box-sizing:border-box}
  html,body{width:852px;height:1200px;overflow:hidden;background:#fff}
  .resume{position:relative;width:852px;height:1200px;font-family:'Ubuntu',sans-serif;color:var(--text)}
  .abs{position:absolute}
  .header-band{left:0;top:0;width:852px;height:189px;background:linear-gradient(120deg,#173a6e 0%,#1f5ea8 45%,#2a6fbf 70%,#1c4f93 100%)}
  .photo-frame{left:306px;top:71px;width:242px;height:236px;background:linear-gradient(#fff 0 118px,var(--grey-frame) 118px)}
  .photo{left:314px;top:79px;width:226px;height:220px;background:var(--blue)}
  .name{left:0;width:852px;top:318px;text-align:center;font-size:33px;color:var(--ink);font-weight:400;letter-spacing:.3px}
  .name b{font-weight:700}
  .title-tag{left:314px;top:366px;width:226px;height:27px;background:var(--blue);color:#fff;font-weight:500;font-size:18px;text-align:center;line-height:27px;letter-spacing:.3px}
  .contact{top:428px;display:flex;align-items:center;gap:12px;font-size:16.5px;color:#333}
  .contact .ico{width:30px;height:30px;border-radius:50%;background:#2b2b2b;display:flex;align-items:center;justify-content:center}
  .rule{left:31px;top:466px;width:792px;height:1.5px;background:var(--rule)}
  .section-icon{left:44px;width:27px;height:27px;border-radius:50%;border:1.5px solid var(--blue);display:flex;align-items:center;justify-content:center}
  .section-title{left:97px;font-size:23px;font-weight:700;color:var(--blue);letter-spacing:.3px}
  .profile-text{left:48px;top:528px;width:466px;font-size:14px;line-height:16.7px}
  .timeline-line{left:57px;width:1.5px;background:#333}
  .node{left:47px;width:21px;height:21px;border-radius:50%;border:1.5px solid #333;background:#fff}
  .node::after{content:"";position:absolute;left:4px;top:4px;width:10px;height:10px;border-radius:50%;background:var(--blue)}
  .dot{left:54px;width:7px;height:7px;border-radius:50%;background:var(--blue)}
  .entry-head{left:97px;font-family:'Open Sans',sans-serif;font-weight:700;font-size:12px;color:#111}
  .entry-sub{left:97px;font-family:'Open Sans',sans-serif;font-size:12.3px;color:#222}
  .skills-title{left:547px;top:489px;font-size:23px;font-weight:700;color:var(--blue);letter-spacing:.3px}
  .skill{left:547px;width:273px}
  .skill .row{display:flex;justify-content:space-between;font-size:12.5px;font-weight:500;color:#111}
  .skill .track{margin-top:5px;height:5px;background:var(--track)}
  .skill .fill{height:5px;background:var(--blue);clip-path:polygon(0 0,calc(100% - 4px) 0,100% 50%,calc(100% - 4px) 100%,0 100%)}
</style>
</head>
<body>
<main class="resume">
  <div class="abs header-band" role="img" aria-label="Background photo of business charts and reports in blue tones"></div>
  <div class="abs photo-frame"></div>
  <div class="abs photo" role="img" aria-label="Portrait photo placeholder"></div>

  <h1 class="abs name"><b>Khalid</b> Nasser Omar <b>Haddad</b></h1>
  <div class="abs title-tag">Senior Project Manager</div>

  <div class="abs contact" style="left:36px">
    <span class="ico"><svg width="16" height="12" viewBox="0 0 16 12"><rect x="1" y="1" width="14" height="10" fill="none" stroke="#fff" stroke-width="1.6"/><path d="M1 1l7 6 7-6M1 11l5-5M15 11l-5-5" fill="none" stroke="#fff" stroke-width="1.4"/></svg></span>
    <span>k.haddad.pm@mailbox.com</span>
  </div>
  <div class="abs contact" style="left:340px">
    <span class="ico"><svg width="16" height="16" viewBox="0 0 24 24"><path fill="#fff" d="M6.6 10.8a15 15 0 006.6 6.6l2.2-2.2c.3-.3.7-.4 1-.2 1.1.4 2.3.6 3.6.6.6 0 1 .4 1 1V20c0 .6-.4 1-1 1A17 17 0 013 4c0-.6.4-1 1-1h3.5c.6 0 1 .4 1 1 0 1.3.2 2.5.6 3.6.1.3 0 .7-.2 1z"/></svg></span>
    <span>+971 500000123</span>
  </div>
  <div class="abs contact" style="left:689px">
    <span class="ico"><svg width="14" height="18" viewBox="0 0 14 18"><path fill="#fff" d="M7 0a7 7 0 00-7 7c0 5 7 11 7 11s7-6 7-11a7 7 0 00-7-7zm0 9.5A2.5 2.5 0 117 4.5a2.5 2.5 0 010 5z"/></svg></span>
    <span>Dubai, UAE</span>
  </div>
  <div class="abs rule"></div>

  <!-- Profile -->
  <div class="abs section-icon" style="top:491px"><svg width="15" height="15" viewBox="0 0 16 16"><circle cx="8" cy="5" r="3.5" fill="#222"/><path d="M1 16c0-4 3-6 7-6s7 2 7 6z" fill="#222"/></svg></div>
  <h2 class="abs section-title" style="top:489px">PROFILE</h2>
  <p class="abs profile-text">Dedicated and multi-faceted professional with advanced analytical, reasoning and problem-solving skills, and offering over 13 years’ insightful experience performing investigative research and analysis to address tactical and strategic business challenges. Adept in the field of Project Management since 6 years with core skills in managing IT &amp; Non-IT Projects, CST Projects etc. Seeking an opportunity to leverage excellent project management, business analysis and data analytics skills and experience with a reputed organization to contribute to strategic business planning</p>

  <!-- Education -->
  <div class="abs section-icon" style="top:700px"><svg width="16" height="14" viewBox="0 0 16 14"><path d="M8 1L0 5l8 4 8-4z" fill="#222"/><path d="M3 7v4c0 1.5 2.5 2.5 5 2.5s5-1 5-2.5V7L8 9.5z" fill="#222"/></svg></div>
  <h2 class="abs section-title" style="top:697px">EDUCATION</h2>
  <div class="abs timeline-line" style="top:755px;height:55px"></div>
  <div class="abs node" style="top:743px"></div>
  <div class="abs node" style="top:799px"></div>
  <div class="abs entry-head" style="top:744px">BECHELOR’S OF COMPUTER SCIENECE</div>
  <div class="abs entry-sub" style="top:762px">Northgate University, Jordan (2006)</div>
  <div class="abs entry-head" style="top:799px">MASTER’S DEGREE IN IT MANAGEMENT</div>
  <div class="abs entry-sub" style="top:816px">Harbourview University, Dubai, UAE (2010)</div>

  <!-- Experience -->
  <div class="abs section-icon" style="top:858px"><svg width="15" height="13" viewBox="0 0 16 14"><rect x="0" y="3" width="16" height="11" rx="1.5" fill="#222"/><rect x="5" y="0.5" width="6" height="3.5" fill="none" stroke="#222" stroke-width="1.4"/><rect x="0" y="7" width="16" height="1" fill="#fff"/></svg></div>
  <h2 class="abs section-title" style="top:856px">EXPERIENCE</h2>
  <div class="abs timeline-line" style="top:912px;height:240px"></div>
  <div class="abs node" style="top:901px"></div>
  <div class="abs dot" style="top:936px"></div>
  <div class="abs node" style="top:968px"></div>
  <div class="abs dot" style="top:1001px"></div>
  <div class="abs dot" style="top:1027px"></div>
  <div class="abs node" style="top:1058px"></div>
  <div class="abs dot" style="top:1089px"></div>
  <div class="abs dot" style="top:1109px"></div>
  <div class="abs dot" style="top:1127px"></div>
  <div class="abs dot" style="top:1147px"></div>

  <div class="abs entry-head" style="top:903px">NATIONAL CIVIL SERVICE AUTHORITY (NCSA)</div>
  <div class="abs entry-sub" style="top:931px">Senior Consultant - Human Resources Systems</div>
  <div class="abs entry-head" style="top:967px">VELTRANA PETROLEUM IRAQ HOLDING B.V.</div>
  <div class="abs entry-sub" style="top:997px">Head – Corporate Affairs</div>
  <div class="abs entry-sub" style="top:1023px">Executive - Performance &amp; Reporting</div>
  <div class="abs entry-head" style="top:1058px">COASTAL CITY COUNCIL</div>
  <div class="abs entry-sub" style="top:1085px">IT Consultant</div>
  <div class="abs entry-sub" style="top:1105px">Business Analyst</div>
  <div class="abs entry-sub" style="top:1123px">Sr. Building System Analyst</div>
  <div class="abs entry-sub" style="top:1143px">Business Support Engineer</div>

  <!-- Core competencies -->
  <h2 class="abs skills-title">CORE COMPETENCIES</h2>
  <div class="abs skill" style="top:539px"><div class="row"><span>English Language</span><span>95%</span></div><div class="track"><div class="fill" style="width:86%"></div></div></div>
  <div class="abs skill" style="top:585px"><div class="row"><span>Arabic Language</span><span>100%</span></div><div class="track"><div class="fill" style="width:100%"></div></div></div>
  <div class="abs skill" style="top:630px"><div class="row"><span>Leadership &amp; Team Building</span><span>90%</span></div><div class="track"><div class="fill" style="width:91%"></div></div></div>
  <div class="abs skill" style="top:676px"><div class="row"><span>Business/IT Analysis</span><span>90%</span></div><div class="track"><div class="fill" style="width:86%"></div></div></div>
  <div class="abs skill" style="top:722px"><div class="row"><span>Requirements Gathering/Analysis</span><span>90%</span></div><div class="track"><div class="fill" style="width:86%"></div></div></div>
  <div class="abs skill" style="top:767px"><div class="row"><span>Business Consulting</span><span>90%</span></div><div class="track"><div class="fill" style="width:91%"></div></div></div>
  <div class="abs skill" style="top:813px"><div class="row"><span>Project Management</span><span>100%</span></div><div class="track"><div class="fill" style="width:100%"></div></div></div>
  <div class="abs skill" style="top:855px"><div class="row"><span>Issues And Crisis Management</span><span>100%</span></div><div class="track"><div class="fill" style="width:100%"></div></div></div>
  <div class="abs skill" style="top:900px"><div class="row"><span>Business Process Re-engineering</span><span>90%</span></div><div class="track"><div class="fill" style="width:86%"></div></div></div>
  <div class="abs skill" style="top:946px"><div class="row"><span>System/Services Support</span><span>95%</span></div><div class="track"><div class="fill" style="width:91%"></div></div></div>
  <div class="abs skill" style="top:991px"><div class="row"><span>Client / Stakeholder Management</span><span>90%</span></div><div class="track"><div class="fill" style="width:86%"></div></div></div>
  <div class="abs skill" style="top:1037px"><div class="row"><span>Event Management</span><span>90%</span></div><div class="track"><div class="fill" style="width:86%"></div></div></div>
  <div class="abs skill" style="top:1083px"><div class="row"><span>Reporting &amp; Documentation</span><span>95%</span></div><div class="track"><div class="fill" style="width:91%"></div></div></div>
  <div class="abs skill" style="top:1128px"><div class="row"><span>Business Process Mapping</span><span>90%</span></div><div class="track"><div class="fill" style="width:86%"></div></div></div>
</main>
</body>
</html>
```